industrial tools need a business card design

Brantor Tools including Cable Tools, Pipe Tools, Rebar Tools, Hydraulic Tools Packing Machine, We need design a business card, Design business card needs to accord with company logo and color, please refer to our website products at the same time:www.brantor-example.com, please see our logo(CDR)in attach,we need cdr type,thanks!

Industry/Entity Type

Industrial

```html
<!DOCTYPE html>
<html lang="en">
<head>
<meta charset="utf-8">
<title>Brantor Tools — Business Card</title>
<link rel="stylesheet" href="https://fonts.googleapis.com/css2?family=Open+Sans:wght@400;600;800&display=swap">
<style>
  :root {
    --backdrop: #e4e4e4;
    --card-grey: #a6a6a6;
    --card-grey-dark: #9a9a9a;
    --band-light: #e9e9e9;
    --band-white: #f6f6f6;
    --ink-dark: #4a4a4a;
    --ink-mid: #5c5c5c;
    --accent-orange: #e8602a;
    --brand-light: #f2f2f2;
  }
  * { box-sizing: border-box; margin: 0; padding: 0; }
  html, body {
    width: 1200px;
    height: 913px;
    overflow: hidden;
    background: var(--backdrop);
    font-family: "Open Sans", Arial, sans-serif;
  }
  .sheet {
    width: 1200px;
    height: 913px;
    display: flex;
    flex-direction: column;
    align-items: center;
    justify-content: center;
    gap: 48px;
  }
  .card {
    position: relative;
    width: 630px;
    height: 360px;
    background: linear-gradient(135deg, var(--card-grey) 0%, var(--card-grey-dark) 100%);
    box-shadow: 0 6px 18px rgba(0,0,0,0.18);
    overflow: hidden;
  }

  /* Front */
  .name-band {
    position: absolute;
    left: 300px;
    top: 42px;
    right: 0;
    height: 70px;
    background: var(--band-light);
    padding: 10px 24px;
  }
  .person-name {
    color: var(--accent-orange);
    font-size: 27px;
    font-weight: 400;
    line-height: 1.1;
  }
  .person-position {
    color: var(--ink-mid);
    font-size: 16px;
    line-height: 1.3;
  }
  .brand-front {
    position: absolute;
    left: 38px;
    top: 150px;
    display: flex;
    align-items: center;
    gap: 12px;
  }
  .brand-mark {
    width: 18px;
    height: 18px;
    background: var(--accent-orange);
  }
  .brand-name {
    font-weight: 800;
    font-size: 46px;
    letter-spacing: 1px;
    color: var(--ink-dark);
    line-height: 1;
  }
  .contact-band {
    position: absolute;
    left: 0;
    right: 0;
    top: 236px;
    height: 78px;
    background: var(--band-light);
    padding: 13px 38px;
    display: grid;
    grid-template-columns: 220px 1fr;
    row-gap: 10px;
    color: var(--ink-dark);
    font-size: 14px;
    font-weight: 600;
  }
  .contact-item {
    display: flex;
    align-items: center;
    gap: 8px;
  }
  .contact-item svg { width: 16px; height: 16px; flex: none; }
  .contact-address { grid-column: 1 / span 2; }

  /* Back */
  .brand-back {
    position: absolute;
    left: 0;
    right: 0;
    top: 120px;
    display: flex;
    justify-content: center;
    align-items: center;
    gap: 16px;
  }
  .brand-back .brand-name {
    font-size: 72px;
    color: var(--brand-light);
  }
  .brand-back .brand-mark {
    width: 26px;
    height: 26px;
  }
  .web-band {
    position: absolute;
    left: 0;
    right: 0;
    bottom: 22px;
    height: 40px;
    background: var(--band-white);
    display: flex;
    align-items: center;
    justify-content: flex-end;
    padding-right: 34px;
    font-size: 14px;
    color: var(--ink-dark);
  }
</style>
</head>
<body>
<main class="sheet">

  <section class="card card-front" aria-label="Business card front">
    <div class="name-band">
      <p class="person-name">Your Name here.</p>
      <p class="person-position">your position here</p>
    </div>

    <div class="brand-front">
      <span class="brand-name">Brantor</span>
      <span class="brand-mark" aria-hidden="true"></span>
    </div>

    <div class="contact-band">
      <div class="contact-item">
        <svg viewBox="0 0 16 16" aria-hidden="true"><rect x="4" y="1" width="8" height="14" rx="1.5" fill="none" stroke="#4a4a4a" stroke-width="1.5"/><circle cx="8" cy="12.5" r="0.9" fill="#4a4a4a"/></svg>
        <span>123-456-7890</span>
      </div>
      <div class="contact-item">
        <svg viewBox="0 0 16 16" aria-hidden="true"><rect x="1" y="3" width="14" height="10" rx="1" fill="#4a4a4a"/><path d="M1.5 3.8 L8 9 L14.5 3.8" fill="none" stroke="#e9e9e9" stroke-width="1.3"/></svg>
        <span>yourname@mail.com</span>
      </div>
      <div class="contact-item contact-address">
        <svg viewBox="0 0 16 16" aria-hidden="true"><path d="M8 1 C4.7 1 3 3.4 3 6 C3 9.5 8 15 8 15 C8 15 13 9.5 13 6 C13 3.4 11.3 1 8 1 Z" fill="#4a4a4a"/><circle cx="8" cy="6" r="2" fill="#e9e9e9"/></svg>
        <span>Your address here</span>
      </div>
    </div>
  </section>

  <section class="card card-back" aria-label="Business card back">
    <div class="brand-back">
      <span class="brand-name">Brantor</span>
      <span class="brand-mark" aria-hidden="true"></span>
    </div>
    <div class="web-band">www.brantor-example.com</div>
  </section>

</main>
</body>
</html>
```